Fresh & Clean *NEW* BUSINESS CARD Needed - OPTOMETRY Clinic/Optical

High-tech optometry practice with 3 doctors seeking new business card.  We provide eye exams, sell, designer glasses/contacts/specialty eyewear and treat ocular diseases.  For our business cards, we are seeking fresh, clean, and crisp design as we grow our team (staffing change).  Simply adding doctors is making the card look busy/cluttered.
 Looking for professional, less cluttered look yet still have our logo, doctor names, phone, address, and website....If possible!  :)
Names:
Marisol Pettigrew, O.D.
Ray Bellamy, O.D.
Nora Vantreese, O.D.
Phone: 555-214-6038
Website: www.BrightLensStudio.example
Address:  418 Harlan P. Moody, Maple Hollow, OR 70000
Ultimately we have the main business card with all doctor sames and that card has two versions  (front is always the same).  The back has two designs (1) displays next appointment time/date, (2) for "general use" (non-appointment.)    I have attached what we have used in the past.  
We also need a design template for each team member in our practice with their name, title, and email.   Those should be designed with the "general use" back (see attached).
**Open to entirely new design so don't feel obligated to keep current format.  Need new perspective!  Also including our watermark and some other design features we have consistently used in past in our portfolio.  Included are two options for logos--vertical and horizontal.
**I also would like to remove "Member of Optic Guild" on our logo if possible**
 Other image files available upon request.

Target Market(s)

New patient & Current Patients

Industry/Entity Type

Optometry

Contact Information for Business Card

High-tech optometry practice with 3 doctors seeking new business card.  We provide eye exams, sell, designer glasses/contacts/specialty eyewear and treat ocular diseases.  For our business cards, we are seeking fresh, clean, and crisp design as we grow our team (staffing change).  Simply adding doctors is making the card look busy/cluttered.  Looking for professional, less cluttered look yet still have our logo, doctor names, phone, address, and website....If possible!  :) Names: Marisol Pettigrew, O.D. Ray Bellamy, O.D. Nora Vantreese, O.D. Phone: 555-214-6038 Website: www.BrightLensStudio.example Address:  418 Harlan P. Moody, Maple Hollow, OR 70000 Ultimately we have the main business card with all doctor sames and that card has two versions  (front is always the same).  The back has two designs (1) displays next appointment time/date, (2) for "general use" (non-appointment.)    I have attached what we have used in the past.   We also need a design template for each team member in our practice with their name, title, and email.   Those should be designed with the "general use" back (see attached). **Open to entirely new design so don't feel obligated to keep current format.  Need new perspective!  Also including our watermark and some other design features we have consistently used in past in our portfolio.  Included are two options for logos--vertical and horizontal. **I also would like to remove "Member of Optic Guild" on our logo if possible**  Other image files available upon request.

Font styles to use
Other font styles liked:
• We have used Montserrat / Yellowtail in the past

Colors

Designer to choose colors to be used in the design.

Requirements
Must have
• Clean & Fresh Design with Logo / Info provided in description. Horizontal orientation. **I have included the CMYK colors we currently have in our logo.
Should not have
• Cluttered

```html
<!DOCTYPE html>
<html lang="en">
<head>
<meta charset="utf-8">
<title>Bright Lens Studio – Business Cards</title>
<link rel="stylesheet" href="https://fonts.googleapis.com/css2?family=Montserrat:wght@300;400;700&display=swap">
<style>
  :root {
    --bg: #3a3a3a;
    --card: #ffffff;
    --slate: #2f3a44;
    --sky: #a9dce8;
    --olive: #6e6a05;
    --amber: #8b5a05;
    --grey: #6f6f6f;
    --ink: #1a1a1a;
  }
  * { margin: 0; padding: 0; box-sizing: border-box; }
  html, body { width: 1200px; height: 875px; overflow: hidden; }
  body {
    background: var(--bg);
    font-family: "Montserrat", sans-serif;
    display: flex;
    flex-direction: column;
    align-items: center;
    justify-content: center;
    gap: 40px;
  }
  .card {
    position: relative;
    width: 660px;
    height: 377px;
    background: var(--card);
    border-radius: 26px;
    overflow: hidden;
  }
  .edge {
    position: absolute;
    left: 0; right: 0;
    height: 12px;
    background: linear-gradient(90deg, var(--slate), var(--sky) 35%, var(--olive) 65%, var(--amber));
  }
  .edge--top { top: 0; }
  .edge--bottom { bottom: 0; }

  .brand {
    position: absolute;
    left: 42px; top: 40px;
    display: flex;
    align-items: center;
    gap: 16px;
  }
  .brand__dot {
    width: 44px; height: 44px;
    border-radius: 50%;
    background: var(--sky);
  }
  .brand__name {
    font-weight: 300;
    font-size: 38px;
    color: var(--grey);
    letter-spacing: 0.5px;
  }

  /* general use card */
  .doctors {
    position: absolute;
    left: 48px; top: 118px;
    list-style: none;
    font-weight: 700;
    font-size: 25px;
    line-height: 1.36;
    color: var(--grey);
  }
  .divider {
    position: absolute;
    left: 48px; right: 48px; top: 246px;
    border-top: 1.5px solid var(--ink);
  }
  .contact {
    position: absolute;
    top: 264px;
    list-style: none;
    font-size: 16px;
    color: var(--ink);
    line-height: 1.7;
  }
  .contact--left { left: 48px; }
  .contact--right { right: 48px; }
  .contact li { display: flex; align-items: center; gap: 10px; }
  .contact svg { width: 16px; height: 16px; flex: none; }
  .address { line-height: 1.35; }

  /* appointment card */
  .appointment__title {
    position: absolute;
    left: 0; right: 0; top: 122px;
    text-align: center;
    font-weight: 700;
    font-size: 22px;
    color: var(--ink);
  }
  .appointment__fields {
    position: absolute;
    left: 50px; right: 50px; top: 182px;
    display: flex;
    gap: 20px;
    font-weight: 300;
    font-size: 20px;
    color: var(--grey);
  }
  .field { flex: 1; display: flex; align-items: baseline; gap: 6px; }
  .field__line { flex: 1; border-bottom: 2px dotted var(--ink); }
  .appointment__notice {
    position: absolute;
    left: 0; right: 0; top: 246px;
    text-align: center;
    font-weight: 700;
    font-size: 22px;
    line-height: 1.3;
    color: var(--ink);
  }
</style>
</head>
<body>

  <section class="card general" aria-label="General use card">
    <div class="edge edge--top" role="img" aria-label="Decorative colour edge"></div>
    <div class="brand">
      <div class="brand__dot"></div>
      <div class="brand__name">Bright Lens Studio</div>
    </div>
    <ul class="doctors">
      <li>Marisol Pettigrew, O.D.</li>
      <li>Ray Bellamy, O.D.</li>
      <li>Nora Vantreese, O.D.</li>
    </ul>
    <div class="divider"></div>
    <ul class="contact contact--left">
      <li>
        <svg viewBox="0 0 16 16"><path d="M3 1.5l3 .5 1 3-2 1.5a9 9 0 0 0 4.5 4.5L11 9l3 1 .5 3-2 1.5C6.5 14 2 9.5 1.5 3.5z" fill="#6e6a05"/></svg>
        555-214-6038
      </li>
      <li>
        <svg viewBox="0 0 16 16"><circle cx="8" cy="8" r="6.5" fill="none" stroke="#6e6a05" stroke-width="1.6"/><path d="M1.5 8h13M8 1.5c-3 3.5-3 9.5 0 13M8 1.5c3 3.5 3 9.5 0 13" fill="none" stroke="#6e6a05" stroke-width="1.2"/></svg>
        www.BrightLensStudio.example
      </li>
    </ul>
    <ul class="contact contact--right">
      <li>
        <svg viewBox="0 0 16 16"><path d="M8 1a5 5 0 0 0-5 5c0 4 5 9 5 9s5-5 5-9a5 5 0 0 0-5-5z" fill="#6e6a05"/><circle cx="8" cy="6" r="2" fill="#fff"/></svg>
        <span class="address">418 Harlan P. Moody,<br>Maple Hollow, OR 70000</span>
      </li>
    </ul>
    <div class="edge edge--bottom" role="img" aria-label="Decorative colour edge"></div>
  </section>

  <section class="card appointment" aria-label="Appointment card">
    <div class="edge edge--top" role="img" aria-label="Decorative colour edge"></div>
    <div class="brand">
      <div class="brand__dot"></div>
      <div class="brand__name">Bright Lens Studio</div>
    </div>
    <h2 class="appointment__title">Your Next Appointment</h2>
    <div class="appointment__fields">
      <div class="field">Date<span class="field__line"></span></div>
      <div class="field">Time<span class="field__line"></span></div>
    </div>
    <p class="appointment__notice">If you unable to keep your appointment<br>kindly give us 24 hour notice</p>
    <div class="edge edge--bottom" role="img" aria-label="Decorative colour edge"></div>
  </section>

</body>
</html>
```